Financial & Tax Strategies

need to get a word press site with existing domains and condense existing content on existing site, make new site dynamic, need mobile too......need to take info from my brimlo website and get modern, relevant site, less verbose on first page, way more things to click and engage people. Would like it to look like this , but with my color scheme and not quite as busy looking. I like much of the content on my tabs. Want maximize by seo capabilities on their as well. The number one thing I can say is to go to my existing website and get content, logo, etc there … www.pineridgealdergroup.com .

Target Market(s)

Those 40 -65, business owners for at least 5 years. Higher net worth.

Number of Pages Required

5+ page

Font styles to use
Sans Serif

Colors
f04a50
e4daeb
ffffff

Requirements
Must have
• seo maximized, lots of places to click on to contact us, calls to action, relevant, conservative, want it to look like this and have the function as well.....slight variation on messaging, but like the simplicity on first view. https://www.dorvettalbrook.com/
Nice to have
• Some area along right side where videos we do will be.
Should not have
• feel too busy, but still have lots of opportunities to engage.

```html
<!DOCTYPE html>
<html lang="en">
<head>
<meta charset="utf-8">
<title>Pine Ridge Alder Group — Financial Advisory</title>
<link href="https://fonts.googleapis.com/css2?family=Open+Sans:wght@400;600;700&family=Playfair+Display:wght@700&family=Oswald:wght@400;500&family=Poppins:wght@400;600&display=swap" rel="stylesheet">
<style>
:root{
  --brand-red:#f04a50;
  --lavender:#e8e0ee;
  --white:#ffffff;
  --ink:#333333;
  --muted:#8a8a8a;
  --tile-grey:#747474;
  --panel-light:#e2e2ea;
  --black:#111111;
  --hero-dark:#2b2a2c;
  --contact-dark:#26323a;
}
*{box-sizing:border-box;margin:0;padding:0}
html,body{width:1200px;height:3365px;overflow:hidden}
body{position:relative;background:var(--white);font-family:"Open Sans",Arial,sans-serif;color:var(--ink)}
.abs{position:absolute}

/* header */
.site-header{left:0;top:0;width:1200px;height:98px;background:var(--white);z-index:2}
.brand{left:70px;top:26px;display:flex;align-items:center;gap:14px}
.brand-dot{width:44px;height:44px;border-radius:50%;background:var(--muted)}
.brand-name{font-family:"Open Sans",sans-serif;font-weight:600;font-size:21px;line-height:24px;color:#555;width:180px}
.main-nav{right:92px;top:38px;display:flex;gap:22px;font-weight:700;font-size:17px;color:#333;letter-spacing:.2px}

/* hero */
.hero{left:0;top:98px;width:1200px;height:604px;background:linear-gradient(100deg,#3c3a3c 0%,#5e5a58 30%,#3a3838 60%,#1f1e20 100%)}
.hero-shade{left:0;top:98px;width:1200px;height:604px;background:rgba(0,0,0,.35)}
.hero-title{left:0;width:1200px;top:332px;text-align:center;font-family:"Playfair Display",Georgia,serif;font-weight:700;font-size:27px;color:var(--brand-red)}
.hero-rule{left:578px;top:376px;width:44px;height:2px;background:var(--brand-red)}
.hero-text{left:240px;width:720px;top:396px;text-align:center;font-size:16px;line-height:20px;color:var(--white)}
.btn-outline{border:2px solid var(--brand-red);color:var(--brand-red);font-weight:600;text-align:center;background:transparent}
.hero-btn{left:530px;top:500px;width:145px;height:47px;line-height:43px;font-size:15px}
.hero-dots{left:574px;top:594px;display:flex;gap:6px}
.hero-dots span{width:12px;height:12px;border-radius:50%;border:1.5px solid #ddd}
.hero-dots span.active{background:var(--brand-red);border-color:var(--brand-red)}
.social{left:1117px;top:360px;display:flex;flex-direction:column;gap:16px}
.social span{width:34px;height:34px;border-radius:50%;border:2px solid var(--white)}

/* story */
.story-mark{left:251px;top:797px;width:150px;height:150px;border-radius:50%;background:#7a7a7a}
.story-title{left:479px;top:762px;font-family:"Playfair Display",Georgia,serif;font-weight:700;font-size:29px;letter-spacing:1.5px;color:#333}
.story-text{left:479px;width:530px;font-size:13.5px;line-height:18px;color:#9a9a9a;font-weight:600}
.story-text.p1{top:815px}
.story-text.p2{top:900px}
.story-btn{left:481px;top:977px;width:93px;height:30px;line-height:26px;font-size:12px}

/* blog */
.blog{left:0;top:1065px;width:1200px;height:582px;background:var(--lavender)}
.blog-intro{left:95px;top:1114px;width:233px;height:233px;background:var(--brand-red);color:var(--white);font-family:"Oswald",sans-serif;font-weight:500;font-size:31px;line-height:36px;padding:78px 0 0 56px}
.blog-intro svg{position:absolute;left:150px;top:174px}
.article-tile{background:var(--tile-grey)}
.article-date{position:absolute;left:0;top:0;background:var(--black);color:var(--white);font-size:10px;font-weight:600;padding:6px 10px}
.article-title{position:absolute;left:8px;top:30px;background:var(--brand-red);color:var(--white);font-family:"Oswald",sans-serif;font-size:22px;line-height:30px;padding:0 8px;text-transform:uppercase}

/* video */
.video-band{left:0;top:1647px;width:1200px;height:570px;background:var(--brand-red)}
.video-frame{left:35px;top:1717px;width:795px;height:349px;background:var(--tile-grey)}
.video-play{left:402px;top:1832px}
.video-label{left:35px;width:795px;top:1930px;text-align:center;color:var(--white);font-size:14px;font-weight:700}
.video-caption{left:35px;top:2066px;width:795px;height:93px;background:var(--panel-light);font-size:12px;line-height:19px;color:#333;padding:14px 30px}
.more-videos{left:868px;top:1714px;width:260px;height:435px;background:var(--white)}
.more-videos-head{left:868px;top:1714px;width:260px;height:42px;line-height:42px;text-align:center;font-size:13px;font-weight:700;color:#888}
.video-item{left:868px;width:260px;height:88px;background:var(--panel-light)}
.video-thumb{position:absolute;left:0;top:0;width:86px;height:88px;background:var(--tile-grey)}
.video-item-title{position:absolute;left:104px;top:14px;font-size:13px;color:#333;font-weight:600}

/* testimonials */
.testi-title{left:0;width:1200px;top:2292px;text-align:center;font-weight:700;font-size:28px;letter-spacing:1.5px;color:#666}
.testi-quote{left:0;width:1200px;top:2338px;text-align:center;font-family:"Playfair Display",serif;font-size:40px;color:#666}
.testi-text{left:150px;width:900px;top:2398px;text-align:center;font-size:17px;line-height:21px;color:#999;font-weight:600}
.testi-role{left:0;width:1200px;top:2486px;text-align:center;font-size:9px;color:#aaa;letter-spacing:1px}
.testi-name{left:0;width:1200px;top:2511px;text-align:center;font-size:10px;font-weight:700;color:#444;letter-spacing:1px}
.avatar{border-radius:50%;background:radial-gradient(circle at 50% 40%,#d9b49a 0%,#8a6a58 65%,#5a4a44 100%)}
.avatar.lead{border:4px solid var(--brand-red)}

/* contact */
.contact-scene{left:0;top:2763px;width:1200px;height:602px;background:linear-gradient(180deg,#2a3a44 0%,#22303a 55%,#3a4a4c 100%)}
.contact-card{left:142px;top:2819px;width:909px;height:546px;background:var(--brand-red)}
.contact-kicker{left:0;width:1200px;top:2876px;text-align:center;font-family:"Poppins",sans-serif;font-size:22px;color:var(--white)}
.contact-title{left:0;width:1200px;top:2915px;text-align:center;font-family:"Poppins",sans-serif;font-weight:600;font-size:37px;letter-spacing:2px;color:var(--white)}
.field{background:var(--white);font-family:"Poppins",sans-serif;font-size:14px;color:#999;padding:10px 14px}
.send-btn{left:533px;top:3191px;width:162px;height:49px;line-height:49px;border-radius:25px;background:var(--white);text-align:center;font-family:"Poppins",sans-serif;font-weight:600;font-size:14px;color:#333;letter-spacing:.5px}
</style>
</head>
<body>

<header class="site-header abs">
  <div class="brand abs"><span class="brand-dot"></span><span class="brand-name">Pine Ridge Alder Group</span></div>
  <nav class="main-nav abs"><span>HOME</span><span>ABOUT</span><span>EXPERTISE</span><span>TEAMS</span><span>TESTIMONIALS</span><span>CONTACT</span></nav>
</header>

<section>
  <div class="hero abs" role="img" aria-label="Photo of business professionals applauding at a meeting"></div>
  <div class="hero-shade abs"></div>
  <h1 class="hero-title abs">We Are A Financial Advisory Company</h1>
  <div class="hero-rule abs"></div>
  <p class="hero-text abs">This is Photoshop's version of Lorem Ipsum. Proin gravida nibh vel velit auctor aliquet. Aenean sollicitudin, lorem quis bibendum auctor, nisi elit consequat ipsum, nec sagittis sem nibh id elit. Duis sed odio sit amet nibh vulputate cursus a sit amet mauris. Morbi accumsan ipsum velit.</p>
  <div class="hero-btn btn-outline abs">LEARN MORE</div>
  <div class="hero-dots abs"><span class="active"></span><span></span><span></span><span></span></div>
  <div class="social abs" aria-label="Social links"><span></span><span></span><span></span></div>
</section>

<section>
  <div class="story-mark abs"></div>
  <h2 class="story-title abs">OUR STORY</h2>
  <p class="story-text p1 abs">This is Photoshop's version of Lorem Ipsum. Proin gravida nibh vel velit auctor aliquet. Aenean sollicitudin, lorem quis bibendum auctor, nisi elit consequat ipsum, nec sagittis sem nibh id elit. Duis sed odio sit amet nibh vulputate cursus</p>
  <p class="story-text p2 abs">Morbi accumsan ipsum velit. Nam nec tellus a odio tincidunt auctor a ornare odio. Sed non mauris vitae erat consequat auctor eu in elit. Class aptent taciti sociosqu ad litora torquent per conubia nostra, per inceptos himenaeos.</p>
  <div class="story-btn btn-outline abs">LEARN MORE</div>
</section>

<section>
  <div class="blog abs"></div>
  <div class="blog-intro abs">BLOG<br>ARTICLES
    <svg width="14" height="22" viewBox="0 0 14 22"><path d="M3 3l8 8-8 8" fill="none" stroke="#fff" stroke-width="2"/></svg>
  </div>
  <article class="article-tile abs" style="left:340px;top:1114px;width:474px;height:233px"><span class="article-date">22 MARCH, 2019</span><span class="article-title">Article One</span></article>
  <article class="article-tile abs" style="left:823px;top:1114px;width:233px;height:233px"><span class="article-date">22 MARCH, 2019</span><span class="article-title">Article Two</span></article>
  <article class="article-tile abs" style="left:95px;top:1358px;width:233px;height:231px"><span class="article-date">22 MARCH, 2019</span><span class="article-title">Article Three</span></article>
  <article class="article-tile abs" style="left:340px;top:1358px;width:230px;height:231px"><span class="article-date">22 MARCH, 2019</span><span class="article-title">Article Four</span></article>
  <article class="article-tile abs" style="left:581px;top:1358px;width:233px;height:231px"><span class="article-date">22 MARCH, 2019</span><span class="article-title">Article Five</span></article>
  <article class="article-tile abs" style="left:823px;top:1358px;width:233px;height:231px"><span class="article-date">22 MARCH, 2019</span><span class="article-title">Article Six</span></article>
</section>

<section>
  <div class="video-band abs"></div>
  <div class="video-frame abs"></div>
  <svg class="video-play abs" width="80" height="80" viewBox="0 0 80 80"><circle cx="40" cy="40" r="37" fill="none" stroke="#fff" stroke-width="3"/><path d="M31 25l24 15-24 15z" fill="none" stroke="#fff" stroke-width="3" stroke-linejoin="round"/></svg>
  <div class="video-label abs">WATCH VIDEO</div>
  <p class="video-caption abs">Lorem Ipsum is simply dummy text of the printing and typesetting industry. Lorem Ipsum has been the industry's standard dummy text ever since the 1500s, when an unknown printer took a galley of type and scrambled it to make a type specimen book. It has survived not only five centuries, but also the leap into electronic typesetting, remaining essentially unchanged.</p>
  <aside>
    <div class="more-videos abs"></div>
    <div class="more-videos-head abs">MORE VIDEOS</div>
    <div class="video-item abs" style="top:1759px"><span class="video-thumb"></span><span class="video-item-title">Lorem Ipsum</span></div>
    <div class="video-item abs" style="top:1856px"><span class="video-thumb"></span><span class="video-item-title">Lorem Ipsum</span></div>
    <div class="video-item abs" style="top:1954px"><span class="video-thumb"></span><span class="video-item-title">Lorem Ipsum</span></div>
    <div class="video-item abs" style="top:2051px"><span class="video-thumb"></span><span class="video-item-title">Lorem Ipsume</span></div>
  </aside>
</section>

<section>
  <h2 class="testi-title abs">TESTIMONIALS</h2>
  <div class="testi-quote abs">&ldquo;</div>
  <p class="testi-text abs">This is Photoshop's version of Lorem Ipsum. Proin gravida nibh vel velit auctor aliquet. Aenean sollicitudin, lorem quis bibendum auctor, nisi elit consequat ipsum, nec sagittis sem nibh id elit. Duis sed odio sit amet nibh vulputate cursus a sit amet mauris. Morbi accumsan ipsum velit. Nam nec tellus a odio tincidunt auctor a ornare odio. Sed non mauris vitae erat consequat auctor eu in elit.</p>
  <div class="testi-role abs">CEO, FOUNDER</div>
  <div class="testi-name abs">JANE MORROW</div>
  <svg class="abs" style="left:346px;top:2620px" width="20" height="28" viewBox="0 0 20 28"><path d="M15 3L5 14l10 11" fill="none" stroke="#888" stroke-width="2"/></svg>
  <svg class="abs" style="left:820px;top:2620px" width="20" height="28" viewBox="0 0 20 28"><path d="M5 3l10 11-10 11" fill="none" stroke="#888" stroke-width="2"/></svg>
  <div class="avatar abs" style="left:402px;top:2605px;width:56px;height:56px" role="img" aria-label="Client portrait"></div>
  <div class="avatar abs" style="left:474px;top:2605px;width:56px;height:56px" role="img" aria-label="Client portrait"></div>
  <div class="avatar lead abs" style="left:549px;top:2589px;width:88px;height:88px" role="img" aria-label="Featured client portrait"></div>
  <div class="avatar abs" style="left:651px;top:2605px;width:56px;height:56px" role="img" aria-label="Client portrait"></div>
  <div class="avatar abs" style="left:728px;top:2605px;width:56px;height:56px" role="img" aria-label="Client portrait"></div>
</section>

<section>
  <div class="contact-scene abs" role="img" aria-label="Photo of a person on a mountain ridge at dusk"></div>
  <div class="contact-card abs"></div>
  <p class="contact-kicker abs">Ready To Invest Differently?</p>
  <h2 class="contact-title abs">CONTACT US</h2>
  <div class="field abs" style="left:219px;top:3017px;width:209px;height:42px">Name</div>
  <div class="field abs" style="left:449px;top:3017px;width:249px;height:42px">Phone</div>
  <div class="field abs" style="left:723px;top:3017px;width:249px;height:42px">Email</div>
  <div class="field abs" style="left:219px;top:3075px;width:760px;height:86px">Message</div>
  <div class="send-btn abs">SEND MESSAGE</div>
</section>

</body>
</html>
```